TableHop website needs a desktop homepage design

We need a desktop homepage design for TableHop.co.uk, a website to help you to find the best restaurants in each main city of Europe, with initial focus on London. It is not a directory with thousands of restaurants and reviews, else lists of top 20 restaurants for each area of the city. TableHop from all around the city will be able to keep an itinerary of where they eat, showing them later funny stats like "this month you really went for pizzas, don't you?". Keep it funny but professional.

A bit of branding has been done but this project give you total freedom to design the homepage of the site. The design must be a mix between minimal, flat and clean layout. The main idea is to keep it simple, easy to use and showing just the necessary elements.

For the font and colour scheme, we would like to use a thin but energetic font using the #E1393A colour as starting point even if you have freedom to slightly modify it. Blacks, greys and whites can be the secondary colours but we are open to introduce another main colour to the site like green, orange or yellow.

A simple wireframe has been attached to help you but the main elements that the page requires are the next:
- Panoramic fancy image in the header to contain the logo and the search form (the fields of the form are specified on the wireframe) and maybe some animated text to fill the right gap.
- List of results (10 results per page) showing the main info for each restaurant: name, thumbnail, location (zone, area), category, price, description, rating (no with stars please) and whatever you want to add that makes sense.
- Right hand sidebar with 3 widgets: Categories, Location and prices.

You can get the icons from glyphbarn.net.

We are open to have some text-shadows, rounded corners, box-shadows but trying to keep it minimal, flat and clean as much as possible. The main attractive of the site are the food/restaurant images.

Target Market(s)

22 - 45 TableHop lovers from the city. busy people that want to disconnect and relax through the food. The don't mind to pay for quality and new experiences. Up to meet new places around them.

Industry/Entity Type

Restaurant

Requirements
Must have
• Panoramic image in the header, restaurants search form as per wireframe, list results with pagination, right hand sidebar with the widgets mention above and a nice footer with extra elements like "latest restaurants, latest tweets, etc.."
Nice to have
• This site will only be supported by the latest browsers so the idea is to have nice CSS3 transitions all around. Have that in mind at the time to design it even if you cannot show it on the design.
Should not have
• Busy backgrounds and unnecessary images that would slow down the page load.

```html
<!DOCTYPE html>
<html lang="en">
<head>
<meta charset="utf-8">
<title>TableHop in London</title>
<link rel="stylesheet" href="https://fonts.googleapis.com/css2?family=Open+Sans:wght@300;400;600&family=Oswald:wght@300;400&family=Kaushan+Script&display=swap">
<style>
:root{
  --red:#e1393a;
  --ink:#222;
  --grey:#777;
  --line:#ddd;
  --paper:#fff;
  --night:#141414;
  --night-2:#0b0b0b;
  --leaf-1:#3f6b2a;
  --leaf-2:#9cbf62;
  --food-1:#c9752c;
  --food-2:#f1d7a8;
}
*{box-sizing:border-box;margin:0;padding:0}
html,body{width:768px;height:1200px;overflow:hidden;background:var(--paper)}
body{font-family:"Open Sans",sans-serif;color:var(--ink);font-size:9px;position:relative}

/* header */
.hero{position:absolute;left:0;top:0;width:768px;height:320px;
  background:radial-gradient(circle at 62% 55%,var(--food-2) 0,#e9c992 14%,transparent 30%),
             radial-gradient(circle at 85% 20%,var(--leaf-2) 0,transparent 40%),
             linear-gradient(135deg,var(--leaf-1),var(--leaf-2) 45%,#6d8f3d 70%,#2c4a1d)}
.search-panel{position:absolute;left:0;top:0;width:240px;height:320px;background:rgba(255,255,255,.93);padding:18px 20px}
.brand{font-family:"Open Sans",sans-serif;font-weight:600;color:var(--red);font-size:17px;display:flex;align-items:center;gap:7px;margin-bottom:22px}
.brand-dot{width:10px;height:10px;border-radius:50%;background:var(--red)}
.field-label{color:var(--grey);font-size:10px;margin:9px 0 4px}
.field{height:26px;border:1px solid #ccc;background:#fff;display:flex;align-items:center;justify-content:space-between;padding:0 8px;font-size:10px}
.field svg{width:13px;height:13px}
.field .pound{color:var(--red);font-weight:600;font-size:13px}
.hero-title{position:absolute;right:36px;top:178px;text-align:right;color:#fff;font-family:"Oswald",sans-serif;font-weight:300;text-shadow:0 1px 4px rgba(0,0,0,.4)}
.hero-title .name{font-size:40px;letter-spacing:2px;line-height:1}
.hero-title .tag{font-size:19px;letter-spacing:1px;margin-top:4px}

/* results */
.results{position:absolute;left:40px;top:338px;width:430px}
.section-title{font-family:"Oswald",sans-serif;font-weight:300;font-size:19px;display:flex;align-items:center;gap:8px;border-bottom:1px solid var(--line);padding-bottom:6px}
.section-title em{font-style:normal;color:var(--red)}
.grid{display:grid;grid-template-columns:205px 205px;gap:18px 20px;margin-top:16px}
.card{border-bottom:2px solid var(--red);height:282px}
.thumb{height:108px;border:1px solid var(--line);background:radial-gradient(ellipse at 50% 55%,var(--food-2) 0,var(--food-1) 45%,#f4f0ea 70%)}
.card-name{color:var(--red);text-align:center;font-size:11px;margin:8px 0 6px}
.facts{display:grid;grid-template-columns:42px 1fr;row-gap:2px;font-size:8.5px;line-height:1.35}
.facts dt{color:var(--red)}
.desc{color:#555;font-size:8.5px;line-height:1.5;margin:8px 0 10px}
.desc b{color:var(--red);font-weight:400}
.rating{display:flex;align-items:center;gap:6px;border-top:1px solid var(--line);padding-top:7px;font-size:8.5px;color:var(--grey)}
.bars{display:flex;gap:2px}
.bars i{width:4px;height:11px;background:var(--red);transform:skewX(-20deg)}
.bars i.off{background:#ccc}
.rating .score{color:var(--red);margin-left:auto}
.pager{display:flex;justify-content:center;gap:10px;margin-top:26px;font-size:11px;color:var(--grey)}
.pager .current{color:var(--red);border-bottom:2px solid var(--red)}

/* sidebar */
.sidebar{position:absolute;left:488px;top:330px;width:250px}
.widget{margin-bottom:26px}
.widget-head{display:flex;height:32px}
.widget-icon{width:32px;background:var(--night);display:flex;align-items:center;justify-content:center}
.widget-title{flex:1;background:var(--red);color:#fff;font-family:"Kaushan Script",cursive;font-weight:400;font-size:15px;display:flex;align-items:center;padding-left:12px}
.widget ul{list-style:none;margin:10px 0 0 44px;font-size:9.5px;line-height:1.9}
.widget li::before{content:"›";color:var(--red);margin-right:6px}

/* footer */
.footer{position:absolute;left:0;top:1046px;width:768px;height:154px;background:var(--night);color:#bbb}
.footer-cols{display:flex;padding:18px 40px 0;gap:30px}
.footer h4{font-family:"Oswald",sans-serif;font-weight:400;font-size:11px;color:#fff;letter-spacing:.5px;margin-bottom:10px}
.footer h4 em{font-style:normal;color:var(--red)}
.latest{width:430px}
.latest-list{display:flex;gap:20px}
.latest-item{display:flex;gap:8px;width:205px}
.latest-thumb{width:52px;height:42px;flex:none;background:radial-gradient(circle,var(--food-2),var(--food-1))}
.latest-item h5{font-size:8px;color:#fff;font-weight:600;margin-bottom:3px}
.latest-item p{font-size:7.5px;line-height:1.45}
.latest-item p b{color:var(--red);font-weight:400}
.tweets{flex:1}
.tweets p{font-size:7.5px;line-height:1.45;margin-bottom:8px}
.tweets span{color:var(--red)}
.footer-base{position:absolute;left:0;bottom:0;width:100%;height:22px;background:var(--night-2)}
</style>
</head>
<body>

<header class="hero" role="img" aria-label="Panoramic photo of a breakfast plate with fresh salad leaves">
  <div class="search-panel">
    <div class="brand"><span class="brand-dot"></span>TableHop in London</div>
    <div class="field-label">What restaurant?</div>
    <div class="field"><span>Brindle</span><svg viewBox="0 0 16 16"><circle cx="7" cy="7" r="5" fill="none" stroke="#e1393a" stroke-width="2"/><path d="M11 11l4 4" stroke="#e1393a" stroke-width="2"/></svg></div>
    <div class="field-label">What kind of food?</div>
    <div class="field"><span>All</span><svg viewBox="0 0 16 16"><path d="M3 6l5 5 5-5" fill="none" stroke="#e1393a" stroke-width="2"/></svg></div>
    <div class="field-label">Where?</div>
    <div class="field"><span>Everywhere</span><svg viewBox="0 0 16 16"><path d="M8 1a5 5 0 0 0-5 5c0 4 5 9 5 9s5-5 5-9a5 5 0 0 0-5-5z" fill="#e1393a"/><circle cx="8" cy="6" r="2" fill="#fff"/></svg></div>
    <div class="field-label">Price?</div>
    <div class="field"><span>All</span><span class="pound">£</span></div>
  </div>
  <div class="hero-title">
    <div class="name">COPPER LADLE</div>
    <div class="tag">THE BEST BREAKFAST IN TOWN</div>
  </div>
</header>

<main class="results">
  <h1 class="section-title">
    <svg width="18" height="18" viewBox="0 0 16 16"><path d="M2 7h3v8H2zM6 7l3-6c1.5 0 2 1 2 2l-.5 3H14c1 0 1.5 1 1.2 2l-1.5 6c-.2.7-.8 1-1.4 1H6z" fill="#e1393a"/></svg>
    BEST RESTAURANT <em>IN LONDON</em>
  </h1>
  <div class="grid">
    <article class="card">
      <div class="thumb" role="img" aria-label="Photo of a restaurant dish"></div>
      <h2 class="card-name">Name of Restaurant</h2>
      <dl class="facts"><dt>Category</dt><dd>Chinese restaurant</dd><dt>Price</dt><dd>£10 - £20</dd><dt>Location</dt><dd>The name of the street 12<br>Name of City, 12345</dd></dl>
      <p class="desc">Fresh seasonal plates, warm service and a cosy room by the river. <b>more</b></p>
      <div class="rating">Average rating<span class="bars"><i></i><i></i><i></i><i></i><i class="off"></i></span><span class="score">4.5 of 5</span></div>
    </article>
    <article class="card">
      <div class="thumb" role="img" aria-label="Photo of a restaurant dish"></div>
      <h2 class="card-name">Name of Restaurant</h2>
      <dl class="facts"><dt>Category</dt><dd>Chinese restaurant</dd><dt>Price</dt><dd>£10 - £20</dd><dt>Location</dt><dd>The name of the street 12<br>Name of City, 12345</dd></dl>
      <p class="desc">Bold flavours, open kitchen and a lively crowd every single night. <b>more</b></p>
      <div class="rating">Average rating<span class="bars"><i></i><i></i><i></i><i></i><i class="off"></i></span><span class="score">4.5 of 5</span></div>
    </article>
    <article class="card">
      <div class="thumb" role="img" aria-label="Photo of a restaurant dish"></div>
      <h2 class="card-name">Name of Restaurant</h2>
      <dl class="facts"><dt>Category</dt><dd>Chinese restaurant</dd><dt>Price</dt><dd>£10 - £20</dd><dt>Location</dt><dd>The name of the street 12<br>Name of City, 12345</dd></dl>
      <p class="desc">Hand made noodles, quick lunch deals and friendly staff near the station. <b>more</b></p>
      <div class="rating">Average rating<span class="bars"><i></i><i></i><i></i><i></i><i class="off"></i></span><span class="score">4.5 of 5</span></div>
    </article>
    <article class="card">
      <div class="thumb" role="img" aria-label="Photo of a restaurant dish"></div>
      <h2 class="card-name">Name of Restaurant</h2>
      <dl class="facts"><dt>Category</dt><dd>Chinese restaurant</dd><dt>Price</dt><dd>£10 - £20</dd><dt>Location</dt><dd>The name of the street 12<br>Name of City, 12345</dd></dl>
      <p class="desc">Slow cooked classics, good wine list and a quiet garden terrace. <b>more</b></p>
      <div class="rating">Average rating<span class="bars"><i></i><i></i><i></i><i></i><i class="off"></i></span><span class="score">4.5 of 5</span></div>
    </article>
  </div>
  <nav class="pager"><span class="current">1</span><span>2</span><span>3</span><span>4</span><span>5</span><span>6</span><span>7</span><span>8</span></nav>
</main>

<aside class="sidebar">
  <section class="widget">
    <div class="widget-head"><span class="widget-icon"><svg width="16" height="16" viewBox="0 0 16 16"><path d="M4 1v6M2 1v4a2 2 0 0 0 4 0V1M4 7v8M11 1c-2 0-2 4-2 6h2v8" fill="none" stroke="#fff" stroke-width="1.5"/></svg></span><h3 class="widget-title">Categories</h3></div>
    <ul><li>Italian restaurants (1)</li><li>Indian restaurants (1)</li></ul>
  </section>
  <section class="widget">
    <div class="widget-head"><span class="widget-icon"><svg width="16" height="16" viewBox="0 0 16 16"><path d="M1 3l4-1 6 2 4-1v11l-4 1-6-2-4 1z" fill="none" stroke="#fff" stroke-width="1.5"/></svg></span><h3 class="widget-title">Location</h3></div>
    <ul><li>Restaurants in West London (1)</li><li>Restaurants in East London (2)</li></ul>
  </section>
  <section class="widget">
    <div class="widget-head"><span class="widget-icon" style="color:#fff;font-size:18px;font-weight:600">£</span><h3 class="widget-title">Prices</h3></div>
    <ul><li>Casual restaurants / 10-20 (1)</li><li>Middle restaurants / 20-30 (2)</li></ul>
  </section>
</aside>

<footer class="footer">
  <div class="footer-cols">
    <section class="latest">
      <h4>LATEST <em>RESTAURANTS</em></h4>
      <div class="latest-list">
        <div class="latest-item"><div class="latest-thumb" role="img" aria-label="Photo of a new restaurant dish"></div><div><h5>NAME OF RESTAURANT</h5><p>A bright new spot serving small plates, natural wines and weekend brunch for everyone. <b>read more</b></p></div></div>
        <div class="latest-item"><div class="latest-thumb" role="img" aria-label="Photo of a new restaurant dish"></div><div><h5>NAME OF RESTAURANT</h5><p>Family run trattoria with fresh pasta daily, a warm welcome and honest prices too. <b>read more</b></p></div></div>
      </div>
    </section>
    <section class="tweets">
      <h4>LATEST <em>TWEETS</em></h4>
      <p>This month you really went for pizzas, didn't you? <span>@tablehop</span></p>
      <p>Three new breakfast places just landed in East London. <span>@tablehop</span></p>
    </section>
  </div>
  <div class="footer-base"></div>
</footer>

</body>
</html>
```